Harlow Auto , a Dealership and Repair Shop in Marengo Iowa

Harlow Auto is a repair shop and auto sales dealership that offers oil changes, alignments, tires, air conditioning work, computer diagnostics. Focused on Vantras, Marlo and Brisk. Small business with less than 10 employees. Billboard sign is in town and not the larger billboard
billboard is 8ft x 18ft

Target Market(s)

General public

Industry/Entity Type

automotive

Font styles to use
Serif
Sans Serif

Colors

Designer to choose colors to be used in the design.

Requirements
Must have
• Located 2 miles north of Marengo. Sales and service. Phone number 319-555-0187
Nice to have
• Picture of a car or truck, or both. picture of wrench
Should not have
• Not sure

```html
<!DOCTYPE html>
<html lang="en">
<head>
<meta charset="utf-8">
<title>Harlow Auto Billboard</title>
<link rel="stylesheet" href="https://fonts.googleapis.com/css2?family=Archivo:wght@600;700;800&display=swap">
<style>
  :root {
    --page-bg: #d9d9d9;
    --brand-blue: #0c3ea8;
    --accent-blue: #1c52d6;
    --ink-black: #0b0b0c;
    --paper-white: #ffffff;
    --truck-light: #e6e7e9;
    --truck-dark: #8d9095;
  }
  html, body {
    margin: 0;
    width: 932px;
    height: 1200px;
    overflow: hidden;
    background: var(--page-bg);
  }
  .billboard {
    position: absolute;
    left: 66px;
    top: 422px;
    width: 800px;
    height: 355px;
    box-shadow: 0 4px 16px rgba(0,0,0,0.18);
    font-family: "Archivo", Arial, sans-serif;
  }
  .billboard-art { display: block; width: 800px; height: 355px; }
  .brand-name { font-weight: 800; fill: var(--paper-white); }
  .brand-town { font-weight: 700; fill: var(--paper-white); }
  .headline-blue { font-weight: 700; fill: var(--accent-blue); }
  .headline-white { font-weight: 800; fill: var(--paper-white); }
  .service-label { font-weight: 700; fill: var(--paper-white); }
  .feature-item { font-weight: 600; fill: var(--paper-white); }
  .phone-number { font-weight: 800; fill: var(--brand-blue); }
</style>
</head>
<body>
  <section class="billboard">
    <svg class="billboard-art" viewBox="0 0 800 355" xmlns="http://www.w3.org/2000/svg">
      <defs>
        <linearGradient id="truckTone" x1="0" y1="0" x2="0" y2="1">
          <stop offset="0" stop-color="var(--truck-light)"/>
          <stop offset="0.7" stop-color="#c9cbce"/>
          <stop offset="1" stop-color="var(--truck-dark)"/>
        </linearGradient>
      </defs>

      <!-- base -->
      <rect class="base" x="0" y="0" width="800" height="355" fill="var(--paper-white)"/>

      <!-- blue brand panel -->
      <polygon class="brand-panel" points="0,0 428,0 321,188 0,188" fill="var(--brand-blue)"/>

      <!-- black message panel -->
      <polygon class="message-panel" points="441,0 800,0 800,286 278,286" fill="var(--ink-black)"/>

      <!-- brand name -->
      <text class="brand-name" x="178" y="78" font-size="50" text-anchor="middle">Harlow</text>
      <text class="brand-name" x="178" y="112" font-size="22" text-anchor="middle" letter-spacing="6">AUTO</text>
      <text class="brand-town" x="178" y="130" font-size="11" text-anchor="middle">Marengo, IA</text>

      <!-- vehicle photo area -->
      <rect x="0" y="150" width="432" height="205" fill="url(#truckTone)" role="img" aria-label="Photo of a silver full-size pickup truck"/>

      <!-- headline -->
      <text class="headline-blue" x="456" y="36" font-size="27" textLength="320" lengthAdjust="spacingAndGlyphs">LOCATED 2 MILES</text>
      <text class="headline-white" x="454" y="87" font-size="62" textLength="322" lengthAdjust="spacingAndGlyphs">NORTH OF</text>
      <text class="headline-white" x="454" y="142" font-size="62" textLength="322" lengthAdjust="spacingAndGlyphs">MARENGO</text>

      <!-- sales and service band -->
      <polygon class="service-band" points="455,189 759,189 748,224 455,224" fill="var(--brand-blue)"/>
      <polygon class="service-slash" points="766,189 771,189 759,224 754,224" fill="var(--paper-white)"/>
      <text class="service-label" x="466" y="215" font-size="24" textLength="272" lengthAdjust="spacingAndGlyphs">SALES AND SERVICE</text>

      <!-- service list -->
      <g class="feature-list">
        <circle cx="461" cy="250" r="5.5" fill="var(--accent-blue)"/>
        <path d="M458.3 250.2 l1.9 1.9 l3.4 -3.6" stroke="var(--ink-black)" stroke-width="1.5" fill="none"/>
        <text class="feature-item" x="471" y="255" font-size="13.5">OIL CHANGES</text>

        <circle cx="598" cy="250" r="5.5" fill="var(--accent-blue)"/>
        <path d="M595.3 250.2 l1.9 1.9 l3.4 -3.6" stroke="var(--ink-black)" stroke-width="1.5" fill="none"/>
        <text class="feature-item" x="608" y="255" font-size="13.5">TIRES</text>

        <circle cx="673" cy="250" r="5.5" fill="var(--accent-blue)"/>
        <path d="M670.3 250.2 l1.9 1.9 l3.4 -3.6" stroke="var(--ink-black)" stroke-width="1.5" fill="none"/>
        <text class="feature-item" x="683" y="255" font-size="13.5">ALIGNMENTS</text>
      </g>

      <!-- phone -->
      <g class="phone-icon">
        <circle cx="467" cy="316" r="12.5" fill="var(--ink-black)"/>
        <path d="M461.5 310.5 c1-1 2-1 2.6 0 l1.4 2.2 c.5.8.3 1.6-.4 2.1 l-.8.6 c.8 1.9 2.2 3.3 4.1 4.1 l.6-.8 c.5-.7 1.3-.9 2.1-.4 l2.2 1.4 c1 .6 1 1.6 0 2.6 c-1.4 1.4-3.5 1.6-5.6.4 c-2.9-1.6-5.2-3.9-6.8-6.8 c-1.2-2.1-1-4.2.6-5.4z" fill="var(--paper-white)"/>
      </g>
      <text class="phone-number" x="486" y="331" font-size="42" textLength="290" lengthAdjust="spacingAndGlyphs">319-555-0187</text>
    </svg>
  </section>
</body>
</html>
```